Doctor in Veterinary Medecine/ veterinarian

I am a vet and would like a buisness card which is simple yet elegant and professional.
My aim is to help as much animals as I can. My main field of expertise are dogs and cats. I would like the card to reflect a "family doctor" feeling.
It should not be the traditional picture of a paw or a dog but yet it should have a sign of a pet on it. I would like to have my name Lina Haddour as well as my profession D.V.M and my number.

Target Market(s)

Lebanese population who have pets

Industry/Entity Type

Doctor

Contact Information for Business Card

Should contain my profession " D.V.M", my full name "Lina Haddour" and my number "0096171552934"

Requirements
Must have
• A certain picture depicting my profession
Nice to have
• Some sort of picture related to pets and animals
Should not have
• A picture of a paw or a dog. I need something more creative

```html
<!DOCTYPE html>
<html lang="en">
<head>
<meta charset="utf-8">
<title>Lina Haddour, D.V.M – Business Card</title>
<link rel="stylesheet" href="https://fonts.googleapis.com/css2?family=Roboto:wght@400;700&display=swap">
<style>
  :root {
    --page-bg: #e9e6e1;
    --card-white: #f7f7f7;
    --violet: #8a3fc2;
    --violet-deep: #6a22a8;
    --lime: #8cc63f;
    --text-light: #ffffff;
    --brand-violet: #8e48c6;
  }
  html, body {
    margin: 0;
    width: 1200px;
    height: 1023px;
    overflow: hidden;
    background: var(--page-bg);
  }
  .business-card {
    position: absolute;
    left: 150px;
    top: 254px;
    width: 900px;
    height: 515px;
    background: var(--card-white);
    box-shadow: 0 18px 40px rgba(0,0,0,0.18);
    overflow: hidden;
    font-family: "Roboto", Arial, sans-serif;
  }
  .card-shapes {
    position: absolute;
    inset: 0;
  }
  .brand-mark {
    position: absolute;
    left: 70px;
    top: 232px;
    display: flex;
    align-items: center;
    gap: 14px;
  }
  .brand-dot {
    width: 30px;
    height: 30px;
    border-radius: 50%;
    border: 3px solid var(--lime);
    box-sizing: border-box;
  }
  .brand-name {
    font-weight: 700;
    font-size: 34px;
    color: var(--brand-violet);
  }
  .contact-block {
    position: absolute;
    left: 585px;
    top: 172px;
    color: var(--text-light);
    white-space: nowrap;
  }
  .holder-name {
    font-weight: 700;
    font-size: 46px;
    line-height: 1.1;
    margin: 0;
    letter-spacing: 0.5px;
  }
  .holder-title {
    font-weight: 700;
    font-size: 21px;
    margin: 10px 0 0;
    letter-spacing: 1px;
  }
  .holder-phone {
    font-weight: 400;
    font-size: 24px;
    margin: 12px 0 0;
    letter-spacing: 1px;
  }
</style>
</head>
<body>
  <div class="business-card">
    <svg class="card-shapes" width="900" height="515" viewBox="0 0 900 515" aria-hidden="true">
      <defs>
        <linearGradient id="violetPanel" x1="0" y1="0" x2="1" y2="1">
          <stop offset="0" stop-color="#9d4fd3"/>
          <stop offset="1" stop-color="#6a22a8"/>
        </linearGradient>
      </defs>
      <path d="M400 0 C 500 160, 470 360, 330 515 L 348 515 C 490 360, 520 160, 420 0 Z" fill="var(--lime)"/>
      <path d="M450 0 C 545 160, 515 360, 380 515 L 900 515 L 900 0 Z" fill="url(#violetPanel)"/>
      <path d="M470 0 C 565 160, 535 360, 400 515 L 408 515 C 543 360, 573 160, 478 0 Z" fill="#ffffff"/>
    </svg>

    <div class="brand-mark">
      <span class="brand-dot"></span>
      <span class="brand-name">Haddour Vet</span>
    </div>

    <div class="contact-block">
      <p class="holder-name">Lina Haddour</p>
      <p class="holder-title">D.V.M</p>
      <p class="holder-phone">009 617 155 2934</p>
    </div>
  </div>
</body>
</html>
```